Business Card Design for a technology company

Our current business card is outdated and stale.

We need a new look and one soon.

We're a telematics (GPS tracking) company based in Australia. Our audiences are transport and logistics company.

Target Market(s)

1. Transport and Logistics Companies
2. Food and Beverage Manufacturers
3. Concrete Businesses

Industry/Entity Type

Logistics

Contact Information for Business Card

Lumen Rove

Font styles to use
Sans Serif

Colors
3276b5
0255a3
85acd3
cfdeed
ffffff

Requirements
Must have
• Logo
• "Premium Suppliers of Real Time Temperature Tracking"
• Contact Name
• Business Title
• Address
• Telephone
• Mobile
• Email
• Website URL
Nice to have
• Visual representation of tracking or maps.
Should not have
• Image of a satellite as currently shown

```html
<!DOCTYPE html>
<html lang="en">
<head>
<meta charset="utf-8">
<title>Lumen Rove Business Card</title>
<link rel="stylesheet" href="https://fonts.googleapis.com/css2?family=Montserrat:wght@400;500;700;800&display=swap">
<style>
  :root {
    --brand-blue: #1d4291;
    --brand-navy: #1a2f63;
    --ink: #2a2a2a;
    --card-back: #e8e9ea;
    --white: #ffffff;
    --stage: #efede8;
  }
  * { margin: 0; padding: 0; box-sizing: border-box; }
  html, body {
    width: 1200px; height: 1190px; overflow: hidden;
    background: var(--stage);
    font-family: "Montserrat", sans-serif;
  }
  .canvas { position: relative; width: 1200px; height: 1190px; }
  .card { position: absolute; left: 202px; width: 788px; overflow: hidden; }
  .card-front { top: 137px; height: 457px; background: var(--brand-blue); }
  .card-back { top: 654px; height: 441px; background: var(--card-back); }

  .front-wordmark {
    position: absolute; left: 90px; top: 132px;
    font-size: 96px; font-weight: 700; line-height: 1;
    color: var(--white); letter-spacing: -1.5px; white-space: nowrap;
  }
  .pill {
    position: absolute; left: 102px; width: 218px; height: 33px;
    background: var(--white); border-radius: 7px;
    color: var(--brand-blue); font-weight: 800; font-size: 16px;
    display: flex; align-items: center; justify-content: center;
  }
  .pill-url { top: 283px; }
  .pill-service { top: 346px; font-size: 15px; }
  .coverage-map {
    position: absolute; left: 496px; top: 245px; width: 182px; height: 176px;
    background: rgba(255,255,255,0.85); border-radius: 24px;
  }

  .contact-name {
    position: absolute; left: 44px; top: 86px;
    font-size: 52px; font-weight: 500; color: var(--brand-blue); letter-spacing: 1px;
    line-height: 1; white-space: nowrap;
  }
  .contact-title {
    position: absolute; left: 44px; top: 148px;
    font-size: 30px; font-weight: 500; color: var(--ink); letter-spacing: 1px; line-height: 1;
  }
  .back-wordmark {
    position: absolute; left: 426px; top: 104px;
    font-size: 50px; font-weight: 700; color: var(--brand-navy); letter-spacing: -1px;
    line-height: 1; white-space: nowrap;
  }
  .divider {
    position: absolute; left: 44px; top: 199px; width: 592px; height: 3px; background: var(--ink);
  }
  .contact-list { list-style: none; }
  .contact-row {
    position: absolute; left: 44px; display: flex; align-items: center;
    font-size: 18px; letter-spacing: 0.3px; color: var(--ink); line-height: 1; white-space: nowrap;
  }
  .contact-row svg { width: 22px; height: 22px; margin-right: 28px; fill: var(--brand-blue); flex: none; }
  .row-phone { top: 222px; }
  .row-mobile { top: 256px; }
  .row-email { top: 285px; }
  .row-address { top: 315px; }
  .tagline {
    position: absolute; left: 0; right: 0; top: 381px; text-align: center;
    font-size: 22.5px; color: var(--brand-blue); line-height: 1;
  }
</style>
</head>
<body>
<div class="canvas">
  <section class="card card-front">
    <div class="front-wordmark">Lumen Rove</div>
    <div class="pill pill-url">lumenrove.com.au</div>
    <div class="pill pill-service">GPS Tracking Systems</div>
    <div class="coverage-map" role="img" aria-label="Map of Australia marked with location pins"></div>
  </section>

  <section class="card card-back">
    <div class="contact-name">Mark Ellison</div>
    <div class="contact-title">DIRECTOR</div>
    <div class="back-wordmark">Lumen Rove</div>
    <div class="divider"></div>
    <ul class="contact-list">
      <li class="contact-row row-phone">
        <svg viewBox="0 0 24 24" aria-hidden="true"><path d="M6.6 10.8c1.4 2.8 3.8 5.1 6.6 6.6l2.2-2.2c.3-.3.7-.4 1-.2 1.1.4 2.3.6 3.6.6.6 0 1 .4 1 1V20c0 .6-.4 1-1 1C10.6 21 3 13.4 3 4c0-.6.4-1 1-1h3.5c.6 0 1 .4 1 1 0 1.3.2 2.5.6 3.6.1.3 0 .7-.2 1l-2.3 2.2z"/></svg>
        <span>+03 1800 555 014</span>
      </li>
      <li class="contact-row row-mobile">
        <svg viewBox="0 0 24 24" aria-hidden="true"><path d="M8 2h8c1.1 0 2 .9 2 2v16c0 1.1-.9 2-2 2H8c-1.1 0-2-.9-2-2V4c0-1.1.9-2 2-2zm0 3v12h8V5H8zm3 13.5v1.5h2v-1.5h-2z"/></svg>
        <span>+03 1800 555 014</span>
      </li>
      <li class="contact-row row-email">
        <svg viewBox="0 0 24 24" aria-hidden="true"><path d="M2 5h20v14H2V5zm2 2v.5l8 5.5 8-5.5V7l-8 5.3L4 7zm0 3v7h16v-7l-8 5.5L4 10z"/></svg>
        <span>sales@lumenrove.com.au</span>
      </li>
      <li class="contact-row row-address">
        <svg viewBox="0 0 24 24" aria-hidden="true"><path d="M12 2c-3.9 0-7 3.1-7 7 0 5.2 7 13 7 13s7-7.8 7-13c0-3.9-3.1-7-7-7zm0 9.5a2.5 2.5 0 1 1 0-5 2.5 2.5 0 0 1 0 5z"/></svg>
        <span>Unit 4, 18 Calder Street Kilsyth VIC 3137 Australia</span>
      </li>
    </ul>
    <p class="tagline">Premium Suppliers of Real Time Temperature Tracking</p>
  </section>
</div>
</body>
</html>
```